Wine Label Design

A wine label for 750ml bottles. Same label for different varieties with the variety / region / vintage to be updated as required.
Brand: Beyond the Ridge
Product Use: Front and Back label suitable for a 750 ml bottle (preferably Burgundy bottles)
Design Brief: Beyond the Ridge is a small winery that produces limited amounts of hand crafted wines that are aimed at the mid to top end of the market and requires a label befitting the work that goes into the creation of the wine. In terms of style i don't have any preconceptions and am open to a broad range of design suggestions at the same level of existing premium brands or innovative brands.
Must Have for Front label
Front Label
Beyond the Ridge
2013
Grampians
Shiraz
750ML (should be in smaller text)
Alc. 14% by Vol. (should be in smaller text)
Must Have for Back Label
Beyond the Ridge
2013
Grampians
Shiraz
www.beyondtheridge.com.au (should be in smaller text)
Product of Australia
Alc.14% by Vol. (should be in smaller text)
Contains preservative 220(should be in smaller text)
Below are some guides for dimensions:
The Front Label Size can be between
100 - 120 mm (Width) x 70 - 85 mm (Height)
The back label size can be between
90 mm (Width) x 70 - 85 mm (Height)
Target Market(s)
Medium to top end of the wine market who require the label to be a reflection of the wine.
Industry/Entity Type
Product
Colors
Designer to choose colors to be used in the design.
Look and feel

```html
<!DOCTYPE html>
<html lang="en">
<head>
<meta charset="utf-8">
<title>Beyond the Ridge – Grampians Shiraz 2013</title>
<link rel="stylesheet" href="https://fonts.googleapis.com/css2?family=Cinzel:wght@600;700&family=Old+Standard+TT:wght@400;700&display=swap">
<style>
  :root {
    --label-bg: #dfcdb3;
    --brand-gold: #9a8058;
    --variety-brown: #7e6846;
    --ink: #1c1a17;
    --vignette-light: #c2a981;
    --vignette-dark: #8c734e;
    --vignette-shadow: #6f5a3c;
  }
  html, body {
    margin: 0;
    padding: 0;
    overflow: hidden;
  }
  .label {
    position: relative;
    width: 1200px;
    height: 1133px;
    background: var(--label-bg);
    overflow: hidden;
  }
  .line {
    position: absolute;
    left: 0;
    width: 100%;
    margin: 0;
    text-align: center;
    white-space: nowrap;
    line-height: 1;
  }
  .brand-name {
    top: 228px;
    font-family: "Cinzel", serif;
    font-weight: 700;
    font-size: 54px;
    letter-spacing: 2px;
    color: var(--brand-gold);
  }
  .vineyard-vignette {
    position: absolute;
    left: 406px;
    top: 294px;
    width: 358px;
    height: 194px;
  }
  .variety {
    font-family: "Cinzel", serif;
    font-weight: 700;
    color: var(--variety-brown);
    font-size: 34px;
    letter-spacing: 3px;
  }
  .variety.region { top: 504px; }
  .variety.grape { top: 559px; }
  .variety.vintage { top: 610px; letter-spacing: 2px; }
  .details {
    font-family: "Cinzel", serif;
    font-weight: 600;
    color: var(--ink);
    font-size: 27px;
    letter-spacing: 3px;
  }
  .details.website { top: 681px; }
  .details.origin { top: 731px; }
  .small-print {
    position: absolute;
    margin: 0;
    font-family: "Old Standard TT", serif;
    color: var(--ink);
    line-height: 1;
    white-space: nowrap;
  }
  .volume {
    left: 197px;
    top: 852px;
    font-size: 22px;
  }
  .alcohol {
    right: 181px;
    top: 850px;
    font-size: 22px;
    letter-spacing: 1px;
  }
  .preservative {
    right: 183px;
    top: 885px;
    font-size: 18px;
    letter-spacing: -0.3px;
    transform: scaleX(0.86);
    transform-origin: right center;
  }
</style>
</head>
<body>
<main class="label">
  <h1 class="line brand-name">BEYOND THE RIDGE</h1>

  <svg class="vineyard-vignette" viewBox="0 0 358 194" role="img" aria-label="Oval vignette of a vineyard landscape with rows of vines, a farmhouse and trees">
    <defs>
      <radialGradient id="vignetteFill" cx="45%" cy="40%" r="65%">
        <stop offset="0%" stop-color="var(--vignette-light)"/>
        <stop offset="100%" stop-color="var(--vignette-dark)"/>
      </radialGradient>
    </defs>
    <ellipse cx="183" cy="100" rx="172" ry="91" fill="var(--vignette-shadow)" opacity="0.55"/>
    <ellipse cx="176" cy="94" rx="172" ry="91" fill="url(#vignetteFill)"/>
  </svg>

  <p class="line variety region">GRAMPIANS</p>
  <p class="line variety grape">SHIRAZ</p>
  <p class="line variety vintage">2013</p>

  <p class="line details website">WWW.BEYONDTHERIDGE.COM.AU</p>
  <p class="line details origin">PRODUCT OF AUSTRALIA</p>

  <p class="small-print volume">750ML</p>
  <p class="small-print alcohol">ALC.14% BY VOL.</p>
  <p class="small-print preservative">CONTAINS PRESERVATIVE 220</p>
</main>
</body>
</html>
```